Creative Photography Business Card

Looking for a unique, creative, elegant, sophisticated and professional business card for my photography business.

I specialise in children, families, modelling, weddings and special event photography

Things to include:
Logo - will attach
Email: hello@mirenholtstudio.com.au
web:www.mirenholtstudio.com.au
Ph: 0438 561 204

I will also upload some of my work that you may like to use.

Please be creative and unique in your designs.

Reason: Currently away for work...finding it hard to give feedback in time for the deadline - sorry.

```html
<!DOCTYPE html>
<html lang="en">
<head>
<meta charset="utf-8">
<title>Miren Holt Studio — Business Card</title>
<link rel="stylesheet" href="https://fonts.googleapis.com/css2?family=Arimo:wght@700&display=swap">
<style>
  :root {
    --page-bg: #2b2b2e;
    --lavender-light: #cfcdec;
    --lavender-dark: #a8a4d8;
    --card-grey: #c9ccdd;
    --frame-white: #f4f4f8;
    --ink-blue: #2d4fa8;
    --ink-dark: #1d1d24;
    --band-purple: #7a57b9;
    --photo-pink: #d86bb8;
    --photo-lilac: #b7a3dc;
    --photo-warm: #e9c7a8;
  }
  * { margin: 0; padding: 0; box-sizing: border-box; }
  html, body { width: 1200px; height: 900px; overflow: hidden; }
  body {
    background: var(--page-bg);
    font-family: "Arimo", Arial, sans-serif;
    font-weight: 700;
    position: relative;
  }
  .card {
    position: absolute;
    left: 280px;
    width: 640px;
    height: 366px;
    overflow: hidden;
    box-shadow: 0 10px 30px rgba(0,0,0,0.5);
  }
  /* Reverse side */
  .card-back {
    top: 70px;
    background: radial-gradient(ellipse at 55% 40%, var(--lavender-light), var(--lavender-dark));
    display: flex;
    align-items: center;
    justify-content: center;
  }
  .brand {
    display: flex;
    align-items: center;
    gap: 18px;
    color: var(--ink-blue);
  }
  .brand-dot {
    border-radius: 50%;
    background: var(--ink-blue);
    flex: none;
  }
  .brand-large .brand-dot { width: 26px; height: 26px; }
  .brand-large .brand-name { font-size: 56px; letter-spacing: 1px; }
  /* Front side */
  .card-front {
    top: 464px;
    background: var(--card-grey);
  }
  .photo-frame {
    position: absolute;
    left: 22px;
    top: 40px;
    width: 360px;
    height: 250px;
    background: var(--frame-white);
    padding: 8px;
    transform: rotate(-9deg);
    box-shadow: 0 3px 8px rgba(0,0,0,0.25);
  }
  .photo-area {
    width: 100%;
    height: 100%;
    background: linear-gradient(135deg, var(--photo-warm) 0%, var(--photo-pink) 45%, var(--photo-lilac) 100%);
  }
  .brand-small {
    position: absolute;
    right: 34px;
    top: 54px;
    gap: 10px;
  }
  .brand-small .brand-dot { width: 14px; height: 14px; }
  .brand-small .brand-name { font-size: 26px; }
  .contact {
    position: absolute;
    right: 34px;
    top: 198px;
    text-align: right;
    color: var(--ink-dark);
    font-size: 14.5px;
    line-height: 24px;
  }
  .band {
    position: absolute;
    left: 0;
    right: 0;
    bottom: 0;
    height: 26px;
    background: var(--band-purple);
  }
</style>
</head>
<body>
  <section class="card card-back">
    <div class="brand brand-large">
      <span class="brand-dot"></span>
      <span class="brand-name">Miren Holt</span>
    </div>
  </section>

  <section class="card card-front">
    <div class="photo-frame">
      <div class="photo-area" role="img" aria-label="Portfolio photo of three smiling children hugging"></div>
    </div>
    <div class="brand brand-small">
      <span class="brand-dot"></span>
      <span class="brand-name">Miren Holt</span>
    </div>
    <div class="contact">
      <p>Email: hello@mirenholtstudio.com.au</p>
      <p>web:www.mirenholtstudio.com.au</p>
      <p>Ph: 0438 561 204</p>
    </div>
    <div class="band"></div>
  </section>
</body>
</html>
```